Life and Personal development life coach needs card design

I need a card design that matches the style and design of my website. I'd like to stay in the same color scheme. Please check out my website for ideas. www.brivelmorcott.com
I have had previous designs for this. I am wondering if you have access to those for more ideas??

```html
<!DOCTYPE html>
<html lang="en">
<head>
<meta charset="UTF-8">
<title>Brivel Morcott – Life Coach Business Card</title>
<link rel="stylesheet" href="https://fonts.googleapis.com/css2?family=Questrial&family=Montserrat:wght@700&display=swap">
<style>
  :root {
    --lime: #9fcd1b;
    --ink: #1d1d1d;
    --name-grey: #3a3a3a;
    --paper: #ffffff;
    --backdrop: #ecebe8;
    --photo-dark: #1f2a4a;
    --photo-light: #d9d2c2;
  }
  * { box-sizing: border-box; margin: 0; padding: 0; }
  html, body { width: 1200px; height: 900px; overflow: hidden; }
  body { background: var(--backdrop); position: relative; font-family: "Questrial", sans-serif; }

  .card {
    position: absolute;
    top: 300px;
    width: 525px;
    height: 300px;
    background: var(--paper);
    border-radius: 22px;
    overflow: hidden;
    box-shadow: 0 6px 18px rgba(0,0,0,0.18);
  }

  /* Front: name side */
  .card--front { left: 50px; text-align: center; }
  .front__name {
    position: absolute; top: 96px; left: 0; right: 0;
    font-family: "Questrial", sans-serif; font-weight: 400;
    font-size: 54px; letter-spacing: 1px; line-height: 1;
    color: var(--name-grey);
  }
  .front__url {
    position: absolute; top: 212px; left: 58px; width: 410px; height: 42px;
    background: var(--lime); border-radius: 21px;
    font-family: "Montserrat", sans-serif; font-weight: 700;
    font-size: 21px; line-height: 42px; color: var(--ink);
  }

  /* Back: contact side */
  .card--back { left: 625px; }
  .back__topband { position: absolute; top: 0; left: 0; right: 0; height: 20px; background: var(--lime); }
  .back__photo {
    position: absolute; top: 26px; left: 22px; width: 250px; height: 172px;
    border: 3px solid var(--lime);
    background: linear-gradient(120deg, var(--photo-light) 0%, #8e8f9a 45%, var(--photo-dark) 100%);
  }
  .back__name {
    position: absolute; top: 86px; left: 288px;
    font-family: "Montserrat", sans-serif; font-weight: 700;
    font-size: 19px; color: var(--lime); letter-spacing: 0.5px;
  }
  .back__role {
    position: absolute; top: 112px; left: 282px; width: 232px; height: 24px;
    border: 2px solid var(--lime); border-radius: 12px;
    font-size: 13px; line-height: 20px; text-align: center; color: var(--ink);
  }
  .pill {
    position: absolute; height: 24px; border-radius: 12px;
    background: var(--lime); color: var(--ink);
    font-size: 14px; line-height: 24px; display: flex; align-items: center; gap: 6px; padding: 0 10px;
  }
  .pill svg { flex: none; }
  .pill--phone { top: 146px; left: 380px; width: 130px; }
  .pill--email { top: 172px; left: 282px; width: 232px; font-size: 13px; }

  .back__hours {
    position: absolute; top: 208px; left: 0; right: 0; height: 76px;
    background: var(--lime); color: var(--paper);
    font-family: "Montserrat", sans-serif; font-weight: 700; font-size: 11px;
  }
  .hours__label { position: absolute; top: 8px; left: 22px; }
  .hours__slot { position: absolute; text-align: center; line-height: 1.4; }
  .hours__slot--weekday { top: 22px; left: 140px; }
  .hours__slot--friday { top: 36px; left: 275px; }
  .hours__slot--weekend { top: 44px; left: 410px; }
  .back__bottomband { position: absolute; bottom: 0; left: 0; right: 0; height: 10px; background: var(--lime); }
</style>
</head>
<body>

<section class="card card--front" aria-label="Card front">
  <h1 class="front__name">BRIVEL MORCOTT</h1>
  <p class="front__url">www.brivelmorcott.com</p>
</section>

<section class="card card--back" aria-label="Card back">
  <div class="back__topband"></div>
  <div class="back__photo" role="img" aria-label="Portrait photograph of the coach wearing a dark hat and jacket"></div>
  <h2 class="back__name">BRIVEL MORCOTT, RN</h2>
  <p class="back__role">TRANSFORMATIONAL LIFE COACH</p>
  <p class="pill pill--phone">
    <svg width="10" height="15" viewBox="0 0 10 15"><rect x="1" y="1" width="8" height="13" rx="1.5" fill="none" stroke="#1d1d1d" stroke-width="1.4"/><circle cx="5" cy="11.5" r="0.9" fill="#1d1d1d"/></svg>
    555-013-4827
  </p>
  <p class="pill pill--email">
    <svg width="16" height="11" viewBox="0 0 16 11"><rect x="0.5" y="0.5" width="15" height="10" fill="#1d1d1d"/><path d="M1 1 L8 6.5 L15 1" fill="none" stroke="#9fcd1b" stroke-width="1.2"/></svg>
    brivel@brivelmorcott.com
  </p>
  <div class="back__hours">
    <p class="hours__label">COACHING HOURS</p>
    <p class="hours__slot hours__slot--weekday">MONDAY - THURSDAY<br>9:00AM - 8:00PM</p>
    <p class="hours__slot hours__slot--friday">FRIDAY<br>9:00AM - 6:00PM</p>
    <p class="hours__slot hours__slot--weekend">SAT - SUNDAY<br>9:00AM - 4:00PM</p>
  </div>
  <div class="back__bottomband"></div>
</section>

</body>
</html>
```